Business Card Design

Motorvane Ledger is an online automotive resource on a national scale specifically targeting lease purchases for new cars. Our Online and app platform allow prospective lease clients to scan a window sticker while at a franchise dealership and instantly receive a lease quote at what we call the sweet spot. Motorvane Ledger offers price transparency during the lease process to allow average people the confidence in the lease process and takes away any fear of the big franchise dealers.
Motorvane ledger allows ordinary lease customers to know they are getting a low price lease and not overpaying. Never overpay again

Industry/Entity Type

Automotive

Contact Information for Business Card

Motorvane Ledger
Martin Sowerby (President of operations)
Phone: 888-247-6031
Cell: 561-384-2706

```html
<!DOCTYPE html>
<html lang="en">
<head>
<meta charset="utf-8">
<title>Motorvane Ledger – Business Card</title>
<link rel="stylesheet" href="https://fonts.googleapis.com/css2?family=Source+Sans+3:ital,wght@0,400;0,600;0,800;1,400&display=swap">
<style>
  :root {
    --canvas: #e8e8e8;
    --paper: #ffffff;
    --ink: #111111;
    --night: #000000;
    --steel-light: #8a9096;
    --steel-mid: #3a3f44;
    --text-light: #f2f2f2;
  }
  * { box-sizing: border-box; margin: 0; padding: 0; }
  html, body {
    width: 1000px; height: 1200px; overflow: hidden;
    background: var(--canvas);
    font-family: "Source Sans 3", sans-serif;
  }
  .card {
    position: absolute; left: 193px; width: 612px; height: 360px;
    background: var(--paper); overflow: hidden;
  }
  .card--front { top: 185px; }
  .card--back { top: 632px; background: var(--night); }

  .rule { position: absolute; left: 48px; width: 516px; }
  .rule--top { top: 115px; }
  .rule--bottom { top: 240px; }

  .wordmark {
    position: absolute; display: flex; align-items: center; gap: 12px;
    color: var(--ink); font-weight: 800; text-transform: uppercase;
    letter-spacing: -0.5px; line-height: 1;
  }
  .wordmark__dot { background: var(--ink); border-radius: 50%; flex: none; }
  .card--front .wordmark { left: 0; right: 0; top: 150px; justify-content: center; font-size: 44px; }
  .card--front .wordmark__dot { width: 30px; height: 30px; }

  .back__band { position: absolute; left: 0; top: 40px; width: 100%; height: 80px; background: var(--paper); }
  .back__band .wordmark { left: 64px; top: 27px; font-size: 24px; gap: 8px; }
  .back__band .wordmark__dot { width: 18px; height: 18px; }

  .person { position: absolute; right: 38px; top: 18px; text-align: right; color: var(--ink); }
  .person__name { font-size: 21px; font-weight: 600; line-height: 1.1; }
  .person__role { font-size: 13px; font-style: italic; }

  .back__photo {
    position: absolute; left: 0; top: 128px; width: 330px; height: 232px;
    background: radial-gradient(ellipse at 40% 45%, var(--steel-light) 0%, var(--steel-mid) 38%, var(--night) 75%);
  }
  .contacts {
    position: absolute; right: 38px; top: 152px; text-align: right;
    color: var(--text-light); font-size: 15px; font-weight: 600; line-height: 1.3;
  }
</style>
</head>
<body>
  <section class="card card--front">
    <svg class="rule rule--top" width="516" height="4" viewBox="0 0 516 4"><path d="M0 2 Q258 0 516 2 Q258 4 0 2Z" fill="#111"/></svg>
    <div class="wordmark"><span class="wordmark__dot"></span><span>Motorvane Ledger</span></div>
    <svg class="rule rule--bottom" width="516" height="4" viewBox="0 0 516 4"><path d="M0 2 Q258 0 516 2 Q258 4 0 2Z" fill="#111"/></svg>
  </section>

  <section class="card card--back">
    <div class="back__band">
      <div class="wordmark"><span class="wordmark__dot"></span><span>Motorvane Ledger</span></div>
      <div class="person">
        <p class="person__name">Martin Sowerby</p>
        <p class="person__role">President of operations</p>
      </div>
    </div>
    <div class="back__photo" role="img" aria-label="Photograph of a silver sports car emerging from darkness under a soft spotlight"></div>
    <div class="contacts">
      <p>Phone: 888-247-6031</p>
      <p>Cell: 561-384-2706</p>
    </div>
  </section>
</body>
</html>
```